Graphic Design for a Info Card

We would like a graphic design for an info card . We would like the colours to correspond to our logo , you can add in the colours navy blue or yellow if you would like. We would like it to have the following information. We want something that really pops. We would like the size to be 4 1/2 x 6 .

ATTENTION!! Delivery Promo! Order from us on the @hopplemeals app or @marlinrunner app on FRIDAYS and receive a FREE Sample of our one of our meal prep meals in your bag!
DID YOU KNOW?! Meal Prep is another great service that we offer. Saving you time, promoting your health, and best of all providing a delicious lunch . You can find more info on our website www.brivoranpantry.example . All orders are available for delivery or pickup!

```html
<!DOCTYPE html>
<html lang="en">
<head>
<meta charset="utf-8">
<title>Brivoran Pantry – Delivery Promo Card</title>
<link rel="stylesheet" href="https://fonts.googleapis.com/css2?family=Anton&family=Oswald:wght@500;700&family=Exo+2:wght@400;600;700&display=swap">
<style>
  :root {
    --green: #8fc01f;
    --navy: #22304f;
    --navy-deep: #1b2740;
    --yellow: #f6ee00;
    --white: #ffffff;
    --grey-text: #8a8d93;
    --plane: #efefef;
  }
  * { margin: 0; padding: 0; box-sizing: border-box; }
  html, body { width: 900px; height: 1200px; overflow: hidden; background: var(--white); }
  .card {
    position: relative; width: 900px; height: 1200px; overflow: hidden;
    font-family: "Exo 2", sans-serif; background: var(--white);
  }
  .header { position: absolute; left: 0; top: 0; width: 900px; height: 355px; }
  .header svg { position: absolute; left: 0; top: 0; }
  .promo-band {
    position: absolute; left: 0; top: 355px; width: 900px; height: 683px;
    background: linear-gradient(180deg, #22304f 0%, #25375a 45%, #2a3b55 70%, #34413f 100%);
  }
  .partner-tile {
    position: absolute; left: 108px; width: 143px; height: 143px;
    background: var(--white); border-radius: 22px;
    display: flex; align-items: center; justify-content: center; text-align: center;
    font-weight: 700; font-size: 22px; line-height: 1.1; color: var(--navy);
  }
  .partner-tile.marlin { top: 411px; }
  .partner-tile.hopple { top: 564px; }
  .order-line {
    position: absolute; left: 300px; top: 410px;
    font-size: 29px; font-weight: 600; line-height: 38px; color: var(--white);
    white-space: nowrap;
  }
  .order-line .accent { color: var(--green); }
  .sample-box {
    position: absolute; left: 279px; top: 556px; width: 506px; height: 140px;
    border: 4px solid var(--green); padding: 18px 26px 0 26px;
    font-size: 31px; font-weight: 400; line-height: 33px; color: var(--white);
  }
  .sample-box .accent { color: var(--green); font-weight: 600; }
  .knowledge { position: absolute; left: 0; top: 740px; }
  .benefit {
    position: absolute; top: 918px; display: flex; gap: 10px;
    font-size: 30px; font-weight: 600; line-height: 35px; color: var(--white);
    white-space: nowrap;
  }
  .benefit svg { flex: none; margin-top: 4px; }
  .benefit.time { left: 113px; }
  .benefit.health { left: 288px; }
  .benefit.lunch { left: 524px; }
  .footer { position: absolute; left: 0; top: 1038px; width: 900px; height: 162px; background: var(--white); }
  .brand {
    position: absolute; left: 28px; top: 60px; display: flex; align-items: center; gap: 12px;
    font-weight: 700; font-size: 38px; color: var(--green); letter-spacing: 1px;
    white-space: nowrap;
  }
  .brand .mark { width: 30px; height: 30px; background: var(--green); }
  .web-tab {
    position: absolute; left: 408px; top: 0; width: 492px; height: 55px;
    background: var(--green); border-bottom-left-radius: 40px;
    font-size: 26px; font-weight: 600; color: var(--white); padding: 12px 0 0 32px;
    white-space: nowrap;
  }
  .web-address {
    position: absolute; left: 442px; top: 74px; width: 448px;
    font-size: 29px; font-weight: 700; color: var(--navy);
    white-space: nowrap; overflow: hidden;
  }
  .fine-print {
    position: absolute; left: 443px; top: 122px;
    font-size: 17px; font-weight: 600; color: var(--grey-text);
    white-space: nowrap;
  }
</style>
</head>
<body>
<main class="card">
  <header class="header">
    <svg width="900" height="355" viewBox="0 0 900 355">
      <polygon points="900,0 720,0 560,320 900,40" fill="var(--plane)"/>
      <polygon points="720,0 470,300 560,320" fill="#f5f5f5"/>
      <text x="94" y="232" textLength="714" lengthAdjust="spacingAndGlyphs" font-family="Anton, sans-serif" font-size="205" fill="#dcdcdc">ATTENTION!!</text>
      <text x="88" y="228" textLength="714" lengthAdjust="spacingAndGlyphs" font-family="Anton, sans-serif" font-size="205" fill="var(--green)">ATTENTION!!</text>
      <text x="91" y="325" textLength="720" lengthAdjust="spacingAndGlyphs" font-family="Oswald, sans-serif" font-weight="700" font-size="92" fill="var(--navy)">DELIVERY PROMO!</text>
    </svg>
  </header>

  <section class="promo-band" role="img" aria-label="Dark wooden table with fresh vegetables and fruit in a heart-shaped bowl"></section>

  <div class="partner-tile marlin">Marlin<br>Runner</div>
  <div class="partner-tile hopple">Hopple</div>

  <p class="order-line">
    <span class="accent">ORDER FROM US on</span> the<br>
    @hopplemeals app or<br>
    @marlinrunner app on <span class="accent">FRIDAYS</span>
  </p>

  <p class="sample-box">Receive a <span class="accent">FREE</span> Sample of our one of our meal prep meals in your bag!</p>

  <svg class="knowledge" width="900" height="170" viewBox="0 0 900 170">
    <text x="153" y="96" textLength="596" lengthAdjust="spacingAndGlyphs" font-family="Anton, sans-serif" font-size="112" fill="var(--yellow)">DID YOU KNOW?!</text>
    <text x="88" y="158" textLength="725" lengthAdjust="spacingAndGlyphs" font-family="Oswald, sans-serif" font-weight="500" font-size="40" fill="var(--white)">Meal Prep is another great service that we offer ;</text>
  </svg>

  <div class="benefit time">
    <svg width="30" height="30" viewBox="0 0 30 30"><circle cx="15" cy="15" r="14" fill="var(--yellow)"/><path d="M15 7v9h6" stroke="var(--navy)" stroke-width="3" fill="none" stroke-linecap="round"/></svg>
    <span>Saving<br>You time</span>
  </div>
  <div class="benefit health">
    <svg width="32" height="30" viewBox="0 0 32 30"><path d="M16 28 C4 19 1 13 1 8.5 A7.5 7.5 0 0 1 16 6 A7.5 7.5 0 0 1 31 8.5 C31 13 28 19 16 28Z" fill="none" stroke="var(--yellow)" stroke-width="3"/><path d="M5 14h6l2-4 3 8 2-4h9" fill="none" stroke="var(--yellow)" stroke-width="2.5"/></svg>
    <span>Promoting<br>Your health</span>
  </div>
  <div class="benefit lunch">
    <svg width="26" height="32" viewBox="0 0 26 32"><path d="M2 1v11a4 4 0 0 0 8 0V1M6 1v30" stroke="var(--yellow)" stroke-width="3" fill="none"/><path d="M17 1c5 0 7 5 7 12h-4v18h-3Z" fill="var(--yellow)"/></svg>
    <span>Providing a<br>Delicious lunch</span>
  </div>

  <footer class="footer">
    <div class="brand"><span class="mark"></span>Brivoran Pantry</div>
    <div class="web-tab">Find More Info On Our Website</div>
    <div class="web-address">www.brivoranpantry.example</div>
    <div class="fine-print">*All orders are available for delivery or pickup!</div>
  </footer>
</main>
</body>
</html>
```